Goodlooking website for a company who is working in the IT consultancy

We want a new website designed in WordPress. You can take www.vantorq.nl as an example. It should be a website with some short blocks of information about the company, nice pictures of our partners and our employees. A job page with a clear filter.

Target Market(s)

B2B

Industry/Entity Type

It Company

Coding

Coded - Design and coding required

Number of Pages Required

5+ page

Font styles to use
Sans Serif

Colors
0455a3
34a7d8

Requirements
Must have
• Check briefing

```html
<!DOCTYPE html>
<html lang="en">
<head>
<meta charset="utf-8">
<title>Halvenor Critical IT Systems</title>
<link rel="stylesheet" href="https://fonts.googleapis.com/css2?family=Audiowide&family=Montserrat:wght@600;700&family=Open+Sans:wght@400;600&display=swap">
<style>
:root{
  --teal:#17a99b;
  --teal-dark:#0f7f76;
  --teal-bright:#1ec3b0;
  --blue:#14a3c7;
  --petrol:#134b55;
  --ink:#333;
  --muted:#555;
  --green:#8bbf3a;
  --panel:#f2f2f2;
  --white:#fff;
}
*{margin:0;padding:0;box-sizing:border-box}
html,body{width:1200px;height:3169px;overflow:hidden}
body{font-family:"Open Sans",Arial,sans-serif;color:var(--ink);background:var(--white);position:relative}
h2.section-title{font-family:"Montserrat",Arial,sans-serif;font-weight:700;font-size:34px;text-align:center;letter-spacing:.5px}
.title-rule{width:80px;height:3px;margin:22px auto 0}

/* header */
.site-header{position:absolute;top:0;left:0;width:1200px;height:93px;background:var(--white);z-index:5}
.brand{position:absolute;left:100px;top:22px;display:flex;align-items:center;gap:14px}
.brand-mark{width:52px;height:52px;border-radius:50%;background:var(--teal-dark)}
.brand-name{font-family:"Montserrat",Arial,sans-serif;font-weight:700;font-size:30px;color:var(--petrol);letter-spacing:2px}
.main-nav{position:absolute;right:100px;top:0;display:flex;height:93px}
.main-nav a{display:flex;align-items:center;padding:0 15px;font-family:"Open Sans",Arial,sans-serif;font-weight:600;font-size:16px;color:#222;text-decoration:none}
.main-nav a.active{background:var(--blue);color:var(--white)}

/* hero */
.hero{position:absolute;top:93px;left:0;width:1200px;height:552px;background:radial-gradient(ellipse at 50% 40%,#6c6a55 0%,#3b3c35 45%,#1e211f 100%)}
.hero-title{position:absolute;top:70px;width:100%;text-align:center;font-family:"Audiowide",Arial,sans-serif;font-weight:400;font-size:44px;line-height:52px;color:var(--white);letter-spacing:2px}
.hero-emblem{position:absolute;left:524px;top:200px;width:152px;height:152px;border-radius:50%;border:10px solid rgba(255,255,255,.75);background:var(--teal-dark)}
.hero-dots{position:absolute;top:432px;left:0;width:100%;display:flex;justify-content:center;gap:6px}
.hero-dots span{width:16px;height:16px;border-radius:50%;background:#bbb}
.hero-dots span.on{background:var(--white)}
.hero-curve{position:absolute;left:0;bottom:0}

.divider-mark{position:absolute;left:572px;top:624px;width:56px;height:56px;border-radius:50%;background:var(--teal-dark);border:4px solid var(--white);box-shadow:0 0 0 1px #ddd}

/* about */
.about{position:absolute;top:715px;left:0;width:1200px;text-align:center}
.about h2{color:var(--teal)}
.about .title-rule{background:var(--teal)}
.about p{width:1000px;margin:30px auto 0;font-size:14px;line-height:27px;color:var(--ink)}
.about p + p{margin-top:16px}
.btn{display:inline-block;background:var(--blue);color:var(--white);font-weight:600;font-size:15px;text-decoration:none;border-radius:3px}
.about .btn{margin-top:34px;width:140px;height:50px;line-height:50px}

/* what we do */
.services{position:absolute;top:1120px;left:0;width:1200px;height:585px;background:linear-gradient(180deg,#1bb19f 0%,#14a493 100%);color:var(--white)}
.services h2{margin-top:68px}
.services .title-rule{background:var(--white)}
.service{position:absolute;top:180px;width:320px;text-align:center}
.service .ring{width:220px;height:220px;margin:0 auto;border-radius:50%;background:var(--teal-dark);border:2px dashed rgba(255,255,255,.6);display:flex;align-items:center;justify-content:center}
.service.mid .ring{background:var(--teal-bright)}
.service .core{width:140px;height:140px;border-radius:50%;background:var(--teal-dark);border:3px solid var(--white);display:flex;align-items:center;justify-content:center}
.service h3{margin-top:32px;font-family:"Montserrat",Arial,sans-serif;font-weight:700;font-size:21px}
.service p{margin:14px auto 0;width:290px;font-size:13.5px;line-height:22px}
.connector{position:absolute;top:285px;height:0;border-top:2px dashed var(--white)}
.connector::before,.connector::after{content:"";position:absolute;top:-7px;width:12px;height:12px;border-radius:50%;background:var(--white)}
.connector::before{left:-6px}.connector::after{right:-6px}

/* jobs */
.jobs{position:absolute;top:1775px;left:0;width:1200px}
.jobs h2{color:var(--teal)}
.jobs .title-rule{background:var(--teal)}
.job-card{position:absolute;width:493px;height:142px;background:var(--panel);box-shadow:0 2px 4px rgba(0,0,0,.25);border-radius:2px}
.job-tag{position:absolute;left:8px;top:20px;height:24px;padding:0 8px;line-height:24px;font-size:11.5px;font-weight:600;color:var(--white);border-radius:2px}
.tag-freelance{background:#7a2a8c}.tag-full{background:#e3161b}.tag-part{background:#ef7c12}.tag-temp{background:#8ebf2f}
.job-main{position:absolute;left:93px;top:14px;width:212px}
.job-title{font-family:"Open Sans",Arial,sans-serif;font-weight:600;font-size:18px;letter-spacing:-.2px;color:var(--teal);white-space:nowrap}
.job-meta{margin-top:6px;font-size:14.5px;line-height:22px;color:var(--muted)}
.job-date{margin-top:4px;font-size:14.5px;font-weight:600;color:var(--green)}
.job-place{position:absolute;left:317px;top:14px}
.job-city{font-family:"Open Sans",Arial,sans-serif;font-weight:600;font-size:18px;letter-spacing:-.2px;color:var(--teal)}
.job-region{margin-top:8px;font-size:12.5px;color:var(--muted)}

/* partners */
.partners{position:absolute;top:2282px;left:0;width:1200px;height:397px;background:var(--petrol);color:var(--white)}
.partners h2{margin-top:65px}
.partners .title-rule{background:var(--white)}
.partner-badge{position:absolute;top:205px;width:210px;height:103px;background:var(--white);display:flex;align-items:center;justify-content:center}
.partner-badge span{display:block;width:110px;height:44px;border-radius:4px;background:#c9d3d6}

/* contact */
.contact{position:absolute;top:2679px;left:0;width:1200px;height:490px;background:var(--panel)}
.contact h2{position:absolute;left:100px;top:62px;font-family:"Montserrat",Arial,sans-serif;font-weight:700;font-size:27px;color:var(--teal)}
.contact .rule-left{position:absolute;left:100px;top:108px;width:90px;height:3px;background:var(--teal)}
.contact-item{position:absolute;left:100px;display:flex;align-items:center;gap:22px;font-size:16px;line-height:27px;color:#222}
.contact-icon{width:48px;height:48px;border-radius:50%;border:2px solid #222;display:flex;align-items:center;justify-content:center;flex:none}
.contact-icon.filled{background:var(--teal);border-color:var(--teal)}
.form-intro{position:absolute;left:484px;top:66px;font-size:17px;font-weight:600;color:#222}
.field{position:absolute;height:41px;border:2px solid #555;background:var(--white);font-size:13px;color:#555;padding:8px 8px}
.contact .btn{position:absolute;left:484px;top:333px;width:118px;height:38px;line-height:38px;text-align:center;font-size:15px}
.footer-rule{position:absolute;left:100px;top:412px;width:1000px;height:1px;background:#ccc}
.copyright{position:absolute;left:100px;top:443px;font-size:14px;font-weight:600;color:#222}
.social{position:absolute;top:432px;width:36px;height:36px;border-radius:50%;border:2px solid #222}
</style>
</head>
<body>

<header class="site-header">
  <div class="brand"><span class="brand-mark"></span><span class="brand-name">HALVENOR</span></div>
  <nav class="main-nav">
    <a class="active" href="#">HOME</a>
    <a href="#">OUR SOLUTIONS</a>
    <a href="#">OUR TEAM</a>
    <a href="#">JOB</a>
    <a href="#">CONTACT US</a>
  </nav>
</header>

<section class="hero" role="img" aria-label="Photo of colleagues joining hands around light bulbs">
  <h1 class="hero-title">HALVENOR CRITICAL IT<br>SYSTEMS</h1>
  <div class="hero-emblem"></div>
  <div class="hero-dots"><span class="on"></span><span></span><span></span><span></span><span></span></div>
  <svg class="hero-curve" width="1200" height="120" viewBox="0 0 1200 120"><path d="M0,0 Q600,220 1200,0 L1200,120 L0,120 Z" fill="#fff"/></svg>
</section>

<div class="divider-mark"></div>

<section class="about">
  <h2 class="section-title">ABOUT US</h2>
  <div class="title-rule"></div>
  <p>Nemo enim ipsam voluptatem quia voluptas sit aspernatur aut odit aut fugit, sed quia consequuntur magni dolores eos qui ratione voluptatem sequi nesciunt. Neque porro quisquam est, qui dolorem ipsum quia dolor sit amet, consectetur, adipisci velit, sed quia non numquam eius modi tempora incidunt ut labore et dolore magnam aliquam quaerat voluptatem.</p>
  <p>Neque porro quisquam est, qui dolorem ipsum quia dolor sit amet, consectetur, adipisci velit, sed quia non numquam eius modi tempora incidunt ut labore et dolore magnam aliquam quaerat voluptatem.</p>
  <a class="btn" href="#">CONTACT US</a>
</section>

<section class="services" role="img" aria-label="Teal tinted photo of a smiling team">
  <h2 class="section-title">WHAT WE DO</h2>
  <div class="title-rule"></div>

  <div class="connector" style="left:366px;width:104px"></div>
  <div class="connector" style="left:718px;width:120px"></div>

  <div class="service" style="left:75px">
    <div class="ring"><div class="core">
      <svg width="64" height="64" viewBox="0 0 64 64" fill="none" stroke="#fff" stroke-width="3"><rect x="18" y="6" width="40" height="28"/><line x1="26" y1="15" x2="50" y2="15"/><line x1="26" y1="22" x2="44" y2="22"/><circle cx="11" cy="22" r="5" fill="#fff"/><path d="M4 46 v-12 h14 v12" fill="#fff"/><circle cx="26" cy="44" r="4" fill="#fff"/><circle cx="40" cy="44" r="4" fill="#fff"/><circle cx="54" cy="44" r="4" fill="#fff"/><path d="M20 60 v-8 h12 v8 M34 60 v-8 h12 v8 M48 60 v-8 h12 v8" fill="#fff"/></svg>
    </div></div>
    <h3>TRAINING</h3>
    <p>Nemo enim ipsam voluptatem quia voluptas sit aspernatur aut odit.</p>
  </div>

  <div class="service mid" style="left:440px">
    <div class="ring"><div class="core">
      <svg width="64" height="64" viewBox="0 0 64 64" fill="none" stroke="#fff" stroke-width="3"><rect x="22" y="6" width="32" height="40"/><line x1="30" y1="16" x2="46" y2="16"/><line x1="30" y1="24" x2="46" y2="24"/><line x1="30" y1="32" x2="40" y2="32"/><circle cx="16" cy="34" r="6" fill="#fff"/><path d="M6 60 v-12 a10 10 0 0 1 20 0 v12 z" fill="#fff"/></svg>
    </div></div>
    <h3>PERSONAL COACHING</h3>
    <p>Nemo enim ipsam voluptatem quia voluptas sit aspernatur aut odit.</p>
  </div>

  <div class="service" style="left:793px">
    <div class="ring"><div class="core">
      <svg width="64" height="64" viewBox="0 0 64 64" fill="none" stroke="#fff" stroke-width="3"><rect x="8" y="8" width="48" height="34"/><polyline points="16,32 26,22 34,28 46,16"/><circle cx="22" cy="50" r="4" fill="#fff"/><circle cx="42" cy="50" r="4" fill="#fff"/><path d="M14 62 v-4 h16 v4 M34 62 v-4 h16 v4"/></svg>
    </div></div>
    <h3>EDUCATION PROJECTS</h3>
    <p>Nemo enim ipsam voluptatem quia voluptas sit aspernatur aut odit.</p>
  </div>
</section>

<section class="jobs">
  <h2 class="section-title">FEATURED JOBS</h2>
  <div class="title-rule"></div>

  <article class="job-card" style="left:100px;top:125px">
    <span class="job-tag tag-freelance">Freelance</span>
    <div class="job-main"><div class="job-title">Sr. Finance Manager</div><div class="job-meta">Martin Vell – Posted<br>by Nordline IT</div><div class="job-date">20 Nov 2017</div></div>
    <div class="job-place"><div class="job-city">Los Angeles</div><div class="job-region">California, United States</div></div>
  </article>

  <article class="job-card" style="left:607px;top:125px">
    <span class="job-tag tag-full">Full-Time</span>
    <div class="job-main"><div class="job-title">HR Manager</div><div class="job-meta">Martin Vell – Posted<br>by Nordline IT</div><div class="job-date">20 Nov 2017</div></div>
    <div class="job-place"><div class="job-city">Chicago</div><div class="job-region">Illinois, United States</div></div>
  </article>

  <article class="job-card" style="left:100px;top:280px">
    <span class="job-tag tag-part">Part-Time</span>
    <div class="job-main"><div class="job-title">Deployment Specialist</div><div class="job-meta">Martin Vell – Posted<br>by Nordline IT</div><div class="job-date">20 Nov 2017</div></div>
    <div class="job-place"><div class="job-city">Mountain View</div><div class="job-region">California, United States</div></div>
  </article>

  <article class="job-card" style="left:607px;top:280px">
    <span class="job-tag tag-temp">Temporary</span>
    <div class="job-main"><div class="job-title">Sr. Finance Manager</div><div class="job-meta">Martin Vell – Posted<br>by Nordline IT</div><div class="job-date">20 Nov 2017</div></div>
    <div class="job-place"><div class="job-city">Los Angeles</div><div class="job-region">California, United States</div></div>
  </article>
</section>

<section class="partners">
  <h2 class="section-title">OUR PARTNERS</h2>
  <div class="title-rule"></div>
  <div class="partner-badge" style="left:136px"><span></span></div>
  <div class="partner-badge" style="left:376px"><span></span></div>
  <div class="partner-badge" style="left:615px"><span></span></div>
  <div class="partner-badge" style="left:855px"><span></span></div>
</section>

<section class="contact">
  <h2>CONTACT US</h2>
  <div class="rule-left"></div>

  <div class="contact-item" style="top:152px">
    <span class="contact-icon"><svg width="20" height="16" viewBox="0 0 20 16"><rect x="1" y="1" width="18" height="14" fill="#222"/><polyline points="1,1 10,9 19,1" fill="none" stroke="#fff" stroke-width="1.6"/></svg></span>
    <span>info@halvenor.nl</span>
  </div>
  <div class="contact-item" style="top:220px">
    <span class="contact-icon filled"><svg width="18" height="24" viewBox="0 0 18 24"><path d="M9 1 a8 8 0 0 1 8 8 c0 6 -8 14 -8 14 s-8 -8 -8 -14 a8 8 0 0 1 8 -8z" fill="none" stroke="#fff" stroke-width="2"/><circle cx="9" cy="9" r="3" fill="#fff"/></svg></span>
    <span>HALVENOR<br>Korenbloemstraat 14<br>3521 KD Utrecht</span>
  </div>
  <div class="contact-item" style="top:310px">
    <span class="contact-icon"><svg width="22" height="22" viewBox="0 0 24 24"><path d="M5 2 l4 0 l2 5 l-3 2 a12 12 0 0 0 7 7 l2 -3 l5 2 l0 4 a3 3 0 0 1 -3 3 A18 18 0 0 1 2 5 a3 3 0 0 1 3 -3z" fill="none" stroke="#222" stroke-width="2"/></svg></span>
    <span>085-3172604</span>
  </div>

  <div class="form-intro">Fill out the form below, and we'll contact you shortly.</div>
  <div class="field" style="left:484px;top:118px;width:291px">First Name</div>
  <div class="field" style="left:809px;top:118px;width:291px">Last Name</div>
  <div class="field" style="left:484px;top:173px;width:291px">Phone Number</div>
  <div class="field" style="left:809px;top:173px;width:291px">E-Mail Address</div>
  <div class="field" style="left:484px;top:229px;width:616px;height:88px">Message</div>
  <a class="btn" href="#">Contact Us</a>

  <div class="footer-rule"></div>
  <div class="copyright">Copyright © 2018 Halvenor. All rights reserved.</div>
  <span class="social" style="left:976px"></span>
  <span class="social" style="left:1020px"></span>
  <span class="social" style="left:1064px"></span>
</section>

</body>
</html>
```